A5 Flyer required for Beach Party

Please see the Brief.doc attachment for full details

we need the text to say:

Abu Dhabi Copper Falcons presents
Sunburst Shore Party @ Mirel Beach

Tickets: 200 AED
LIVE DJ
Beer and cocktails for 4 hours.
Ticket holders received 30% discount on Food and Beverage all day.
Hawaiian Tropical Fancy Dress - prize for the best dressed.

```html
<!DOCTYPE html>
<html lang="en">
<head>
<meta charset="utf-8">
<title>Sunburst Shore Party – Cocktail Party Flyer</title>
<link rel="stylesheet" href="https://fonts.googleapis.com/css2?family=Passion+One:wght@700&family=Kaushan+Script&family=Patrick+Hand&family=Tinos:wght@700&family=Quicksand:wght@500&display=swap">
<style>
  :root {
    --canvas: #ffffff;
    --ink-white: #ffffff;
    --teal: #3a8f8c;
    --teal-script: #3c9c98;
    --logo-gold: #c9a46a;
    --icon-blue: #4a78b8;
    --icon-grey: #6b7785;
  }
  * { box-sizing: border-box; margin: 0; padding: 0; }
  html, body {
    width: 1200px; height: 900px; overflow: hidden;
    background: var(--canvas);
  }
  .flyer {
    position: absolute; left: 285px; top: 8px;
    width: 617px; height: 875px; overflow: hidden;
  }
  .beach-scene {
    position: absolute; inset: 0;
    background:
      radial-gradient(ellipse 45% 35% at 8% 30%, rgba(70,70,40,.75), transparent 70%),
      radial-gradient(ellipse 30% 25% at 12% 62%, rgba(150,90,40,.55), transparent 70%),
      radial-gradient(ellipse 40% 20% at 60% 50%, rgba(120,110,60,.5), transparent 70%),
      radial-gradient(ellipse 60% 40% at 85% 85%, rgba(110,205,210,.9), transparent 70%),
      radial-gradient(ellipse 70% 35% at 25% 90%, rgba(245,225,150,.95), transparent 75%),
      linear-gradient(180deg, #d8c99a 0%, #bcd8cf 25%, #a9d3cf 50%, #cfe0b8 68%, #eedb98 85%, #e9d58e 100%);
  }
  .event-date {
    position: absolute; top: 22px; width: 100%; text-align: center;
    font-family: 'Patrick Hand', cursive; font-size: 27px;
    letter-spacing: 2px; color: var(--ink-white);
  }
  .club-mark {
    position: absolute; left: 150px; top: 100px; width: 112px;
    display: flex; flex-direction: column; align-items: center; gap: 6px;
  }
  .club-mark .mark-dot {
    width: 44px; height: 44px; border-radius: 50%;
    background: var(--ink-white);
  }
  .club-mark .mark-name {
    font-family: 'Tinos', serif; font-weight: 700; font-size: 16px;
    line-height: 1.1; text-align: center; color: var(--ink-white);
  }
  .venue-mark {
    position: absolute; left: 322px; top: 118px; width: 160px;
    text-align: center;
    font-family: 'Quicksand', sans-serif; font-weight: 500;
    font-size: 34px; line-height: 1.05; color: var(--logo-gold);
  }
  .headline {
    position: absolute; left: 0; width: 100%; text-align: center;
    font-family: 'Passion One', sans-serif; font-weight: 700;
    color: var(--ink-white); opacity: .93; line-height: 1;
    text-transform: uppercase;
  }
  .headline-beach { top: 228px; font-size: 180px; letter-spacing: 6px; }
  .headline-party { top: 380px; font-size: 165px; letter-spacing: 4px; }
  .subtitle {
    position: absolute; top: 568px; width: 100%; text-align: center;
    font-family: 'Kaushan Script', cursive; font-weight: 400; font-size: 58px;
    line-height: 1; color: var(--teal-script);
  }
  .details {
    position: absolute; top: 668px; left: 0; width: 100%;
    text-align: center; font-family: 'Tinos', serif; font-weight: 700;
    color: var(--teal); font-size: 16px; line-height: 20px;
  }
  .contact-list {
    position: absolute; top: 754px; left: 0; width: 100%;
    list-style: none; text-align: center;
    font-family: 'Tinos', serif; font-weight: 700;
    color: var(--teal); font-size: 17px;
  }
  .contact-list li {
    height: 29px; display: flex; justify-content: center;
    align-items: center; gap: 6px;
  }
  .contact-item { display: inline-flex; align-items: center; gap: 5px; margin: 0 3px; }
  .icon-square {
    width: 21px; height: 21px; border-radius: 3px;
    background: var(--icon-grey); display: inline-block;
  }
  .icon-square.is-blue { background: var(--icon-blue); }
  .contact-list svg { display: block; }
</style>
</head>
<body>
  <main class="flyer">
    <div class="beach-scene" role="img" aria-label="Blurred tropical beach photo with palm trees, pale sky, turquoise sea and sand"></div>

    <p class="event-date">Friday 26th September</p>

    <div class="club-mark">
      <span class="mark-dot"></span>
      <span class="mark-name">Abu Dhabi Copper Falcons</span>
    </div>

    <div class="venue-mark">Mirel Beach</div>

    <h1 class="headline headline-beach">Beach</h1>
    <p class="headline headline-party">Party</p>

    <h2 class="subtitle">Cocktail Party</h2>

    <p class="details">
      Abu Dhabi Copper Falcons presents Sunburst Shore Party @ Mirel Beach<br>
      Tickets: 200 AED · LIVE DJ · Beer and cocktails for 4 hours<br>
      Ticket holders receive 30% discount on Food and Beverage all day<br>
      Hawaiian Tropical Fancy Dress – prize for the best dressed
    </p>

    <ul class="contact-list">
      <li>
        <span>For more information :</span>
        <span class="contact-item">
          <svg width="24" height="20" viewBox="0 0 24 20" aria-hidden="true">
            <rect x="1" y="2" width="22" height="16" rx="1" fill="var(--icon-blue)"/>
            <path d="M1 3 L12 11 L23 3" fill="none" stroke="#fff" stroke-width="1.6"/>
          </svg>
          info@mirelbeach.ae
        </span>
      </li>
      <li>
        <span class="contact-item"><span class="icon-square"></span>@mirelbeach</span>
        <span class="contact-item"><span class="icon-square"></span>@mirelbeach</span>
        <span class="contact-item"><span class="icon-square is-blue"></span>/mirelbeach</span>
      </li>
      <li>
        <span class="contact-item"><span class="icon-square"></span>PIN : 61827340</span>
        <span class="contact-item">Chat : MirelBeach</span>
      </li>
      <li>
        <span class="contact-item">
          <svg width="22" height="22" viewBox="0 0 22 22" aria-hidden="true">
            <circle cx="11" cy="11" r="11" fill="var(--icon-blue)"/>
            <path d="M8 14 L14 8" stroke="#fff" stroke-width="1.8" stroke-linecap="round"/>
            <rect x="4.5" y="10.5" width="7" height="4.5" rx="2.2" transform="rotate(-45 8 12.7)" fill="none" stroke="#fff" stroke-width="1.5"/>
            <rect x="10.5" y="7" width="7" height="4.5" rx="2.2" transform="rotate(-45 14 9.2)" fill="none" stroke="#fff" stroke-width="1.5"/>
          </svg>
          www.mirelbeach.ae
        </span>
      </li>
    </ul>
  </main>
</body>
</html>
```